Online Course Page

We are building a video based online course page. This project is for only the actual page that the student will watch the videos at. They will watch one vide at a time. Once one video lesson is completed then they can move to the next video lesson. The page will need to show the video player. (Main feature.) The list of lessons in the course. Instructor information. Profile picture and bio of the instructor. A Live chat button that will initiate a chat in real-time with the instructor.

The winning designer will also be asked to to design the dashboard area and other aspects of the user interface as an additional project.

Target Market(s)

Adults

Number of Pages Required

1 page

Colors
9bcb3c

Requirements
Must have
• Our logo is attached. Green and grey are our colors. Should feel modern, clean and be simple to navigate. The site will be responsive so the layout should work well on mobile devices.

```html
<!DOCTYPE html>
<html lang="en">
<head>
<meta charset="utf-8">
<title>LearnHarbor – Online Video Courses</title>
<link rel="stylesheet" href="https://fonts.googleapis.com/css2?family=Roboto:wght@400;500;700&family=Questrial&display=swap">
<style>
:root{
  --green:#8cc540;
  --green-dark:#76ad33;
  --green-mid:#80b83a;
  --ink:#1d1d1d;
  --text:#333;
  --muted:#555;
  --header-bg:#f6f7f9;
  --card-bg:#f3f3f3;
  --dark:#1e1f1f;
  --footer:#333;
  --white:#fff;
}
*{box-sizing:border-box;margin:0;padding:0}
html,body{width:1200px;height:2219px;overflow:hidden}
body{position:relative;background:var(--white);font-family:'Roboto',Arial,sans-serif;color:var(--text)}
.abs{position:absolute}

/* header */
.site-header{position:absolute;left:0;top:0;width:1200px;height:92px;background:var(--header-bg)}
.brand{position:absolute;left:142px;top:26px;display:flex;align-items:center;gap:10px;font-family:'Roboto',sans-serif;font-weight:700;font-size:30px;color:var(--green-dark)}
.brand-dot{width:30px;height:30px;border-radius:50%;background:var(--green)}
.contact{position:absolute;left:725px;top:28px;display:flex;gap:12px;align-items:center;font-size:13px;line-height:17px;color:var(--ink)}
.live-help{position:absolute;left:932px;top:28px;width:68px;height:34px;border:2px solid var(--ink);border-radius:5px;font-weight:700;font-size:14px;line-height:30px;text-align:center;color:var(--ink)}
.live-help b{color:var(--green-dark)}
.menu-btn{position:absolute;left:1028px;top:28px;width:30px;height:30px;border:2px solid var(--ink);border-radius:5px;padding:7px 6px;display:flex;flex-direction:column;justify-content:space-between}
.menu-btn i{display:block;height:2px;background:var(--green-dark)}

/* hero */
.hero{position:absolute;left:0;top:92px;width:1200px;height:456px;background:linear-gradient(90deg,#e9dec6 0%,#e6dccb 38%,#d9d3cb 60%,#cfc8c0 100%)}
.hero-title{position:absolute;left:180px;top:180px;font-family:'Questrial',sans-serif;font-weight:700;font-size:27px;line-height:36px;color:#2b2b2b}

/* section heads */
.section-title{position:absolute;left:0;width:1200px;text-align:center;font-weight:500;font-size:30px;color:var(--ink)}
.section-title span{color:var(--green)}
.section-title.light{color:var(--white)}
.rule{position:absolute;left:557px;width:86px;height:2px;background:var(--green)}

/* courses */
.course{position:absolute;top:687px;width:288px;height:420px;background:var(--card-bg)}
.course-photo{height:205px;background:linear-gradient(135deg,#b9c2c8,#d9d2c9 60%,#c87e66)}
.price{position:absolute;right:26px;top:186px;width:48px;height:48px;border-radius:50%;background:var(--green);color:var(--white);font-size:13px;font-weight:500;line-height:48px;text-align:center}
.course-cat{position:absolute;top:228px;width:100%;text-align:center;color:var(--green);font-size:12px}
.course-name{position:absolute;top:245px;width:100%;text-align:center;font-weight:700;font-size:15px;color:var(--ink)}
.rating{position:absolute;top:274px;width:100%;display:flex;justify-content:center;align-items:center;gap:10px;font-size:11px;color:var(--ink)}
.stars{color:var(--green);font-size:13px;letter-spacing:1px;padding-right:10px;border-right:1px solid #999}
.course-desc{position:absolute;top:303px;left:20px;right:20px;text-align:center;font-size:12px;line-height:18px;color:var(--ink)}
.course-stats{position:absolute;top:364px;left:0;right:0;height:56px;border-top:1px solid #ddd;display:flex}
.stat{flex:1;text-align:center;padding-top:11px;font-size:11px;line-height:18px;color:var(--ink);border-right:1px solid #ddd}
.stat:last-child{border-right:0}
.stat b{display:block;font-weight:500}

/* video lessons */
.lessons-band{position:absolute;left:0;top:1172px;width:1200px;height:564px;background:linear-gradient(180deg,#3a3a38 0%,#232423 45%,#1a1b1b 100%)}
.player{position:absolute;left:141px;top:1314px;width:917px;height:358px;background:linear-gradient(135deg,#7e7a70 0%,#6b6c6a 45%,#3d3f41 100%)}
.lesson-list{position:absolute;left:141px;top:1314px;width:327px;height:358px;background:var(--green-mid)}
.lesson{position:absolute;left:0;width:327px;height:86px;display:flex;align-items:center;gap:12px;padding-left:24px;font-family:'Questrial',sans-serif;font-size:12.5px;line-height:17px;color:var(--white)}
.lesson:nth-child(odd){background:var(--green)}
.lesson:nth-child(even){background:var(--green-dark)}
.lesson b{font-family:'Roboto',sans-serif;font-weight:700;font-size:13px;display:block}
.play{flex:none;width:36px;height:36px;border:2px solid var(--ink);border-radius:50%;display:flex;align-items:center;justify-content:center}
.list-arrow{position:absolute;left:157px;width:0;height:0;border-left:6px solid transparent;border-right:6px solid transparent}

/* instructors */
.instructor{position:absolute;top:1875px;width:214px;height:241px;background:linear-gradient(180deg,#e4e4e4,#d7d7d7)}
.instructor-photo{position:absolute;left:0;top:0;width:100%;height:191px;background:linear-gradient(180deg,#e2e2e2,#c9cfd6)}
.name-bar{position:absolute;left:0;bottom:0;width:100%;height:50px;background:rgba(60,60,60,.72);color:var(--white);text-align:center;padding-top:9px;font-size:12px;line-height:16px}
.name-bar b{display:block;font-weight:700;font-size:13px}
.instructor.active{background:#3b3b3b}
.active-frame{position:absolute;left:8px;top:8px;right:8px;bottom:8px;border:2px solid var(--green);text-align:center;color:var(--white);padding-top:55px}
.active-frame b{display:block;font-size:13px;font-weight:700}
.active-frame small{display:block;font-size:11px;margin-top:2px}
.active-frame p{font-family:'Questrial',sans-serif;font-size:12px;line-height:18px;margin-top:14px}
.socials{display:flex;justify-content:center;gap:22px;margin-top:18px}
.socials i{width:10px;height:10px;border-radius:50%;background:var(--white)}

/* footer */
.site-footer{position:absolute;left:0;top:2180px;width:1200px;height:39px;background:var(--footer);color:#ddd;font-size:11px}
.site-footer p{position:absolute;left:142px;top:13px}
.footer-social{position:absolute;left:944px;top:9px;display:flex;gap:5px}
.footer-social i{width:22px;height:22px;border-radius:50%}
</style>
</head>
<body>

<header class="site-header">
  <div class="brand"><span class="brand-dot"></span>LearnHarbor</div>
  <div class="contact">
    <svg width="28" height="22" viewBox="0 0 28 22" aria-hidden="true"><rect x="1" y="3" width="26" height="18" fill="none" stroke="#76ad33" stroke-width="2"/><path d="M1 3l13 10 13-10" fill="none" stroke="#76ad33" stroke-width="2"/></svg>
    <div>Email:<br>info@learnharbor.com</div>
  </div>
  <div class="live-help">Live <b>Help</b></div>
  <div class="menu-btn"><i></i><i></i><i></i></div>
</header>

<section class="hero" role="img" aria-label="Photo of a smiling student with headphones taking notes beside a laptop">
  <h1 class="hero-title">We Provide Online Video<br>Based Education Training</h1>
</section>

<h2 class="section-title" style="top:602px">Our Popular <span>Courses</span></h2>
<div class="rule" style="top:655px"></div>

<article class="course" style="left:141px">
  <div class="course-photo" role="img" aria-label="Photo of a student working at a desktop computer"></div>
  <div class="price">$350</div>
  <div class="course-cat">Science</div>
  <h3 class="course-name">Lorem Ipsum Dolor</h3>
  <div class="rating"><span class="stars">★★★★★</span>39 Reviews</div>
  <p class="course-desc">Lorem ipsum dolor sit amet, consectetuer adipiscing elit, sed diam nonummy.</p>
  <div class="course-stats"><div class="stat"><b>Course Time</b>4 Years</div><div class="stat"><b>Course Student</b>88</div><div class="stat"><b>Class Duration</b>8.30-4.00</div></div>
</article>
<article class="course" style="left:456px">
  <div class="course-photo" role="img" aria-label="Photo of a student writing notes next to a laptop"></div>
  <div class="price">$350</div>
  <div class="course-cat">Science</div>
  <h3 class="course-name">Lorem Ipsum Dolor</h3>
  <div class="rating"><span class="stars">★★★★★</span>39 Reviews</div>
  <p class="course-desc">Lorem ipsum dolor sit amet, consectetuer adipiscing elit, sed diam nonummy.</p>
  <div class="course-stats"><div class="stat"><b>Course Time</b>4 Years</div><div class="stat"><b>Course Student</b>88</div><div class="stat"><b>Class Duration</b>8.30-4.00</div></div>
</article>
<article class="course" style="left:771px">
  <div class="course-photo" role="img" aria-label="Photo of a student using a tablet in a classroom"></div>
  <div class="price">$350</div>
  <div class="course-cat">Science</div>
  <h3 class="course-name">Lorem Ipsum Dolor</h3>
  <div class="rating"><span class="stars">★★★★★</span>39 Reviews</div>
  <p class="course-desc">Lorem ipsum dolor sit amet, consectetuer adipiscing elit, sed diam nonummy.</p>
  <div class="course-stats"><div class="stat"><b>Course Time</b>4 Years</div><div class="stat"><b>Course Student</b>88</div><div class="stat"><b>Class Duration</b>8.30-4.00</div></div>
</article>

<section class="lessons-band" role="img" aria-label="Dimmed background photo of students in a lecture"></section>
<h2 class="section-title light" style="top:1228px">Video <span>Lessons</span></h2>
<div class="rule" style="top:1280px"></div>

<div class="player" role="img" aria-label="Video player showing a student working on a laptop outdoors"></div>
<div class="lesson-list">
  <div class="lesson" style="top:6px"><span class="play"><svg width="12" height="14" viewBox="0 0 12 14"><path d="M1 1l10 6-10 6z" fill="none" stroke="#1d1d1d" stroke-width="1.5"/></svg></span><div><b>Lesson 1</b>Lorem ipsum dolor sit amet, consectetuer adipiscing elit, sed diam nonummy.</div></div>
  <div class="lesson" style="top:92px"><span class="play"><svg width="12" height="14" viewBox="0 0 12 14"><path d="M1 1l10 6-10 6z" fill="none" stroke="#fff" stroke-width="1.5"/></svg></span><div><b>Lesson 2</b>Lorem ipsum dolor sit amet, consectetuer adipiscing elit, sed diam nonummy.</div></div>
  <div class="lesson" style="top:178px"><span class="play"><svg width="12" height="14" viewBox="0 0 12 14"><path d="M1 1l10 6-10 6z" fill="none" stroke="#fff" stroke-width="1.5"/></svg></span><div><b>Lesson 3</b>Lorem ipsum dolor sit amet, consectetuer adipiscing elit, sed diam nonummy.</div></div>
  <div class="lesson" style="top:264px"><span class="play"><svg width="12" height="14" viewBox="0 0 12 14"><path d="M1 1l10 6-10 6z" fill="none" stroke="#fff" stroke-width="1.5"/></svg></span><div><b>Lesson 4</b>Lorem ipsum dolor sit amet, consectetuer adipiscing elit, sed diam nonummy.</div></div>
  <span class="list-arrow" style="top:0;border-bottom:5px solid #fff"></span>
  <span class="list-arrow" style="top:352px;border-top:5px solid #fff"></span>
</div>

<h2 class="section-title" style="top:1791px">About <span>Instructor</span></h2>
<div class="rule" style="top:1843px"></div>

<article class="instructor" style="left:141px">
  <div class="instructor-photo" role="img" aria-label="Portrait of an instructor in a white shirt and tie"></div>
  <div class="name-bar"><b>Martin Hale</b>Vice Chancellor</div>
</article>
<article class="instructor" style="left:374px">
  <div class="instructor-photo" role="img" aria-label="Portrait of an instructor in a green blazer"></div>
  <div class="name-bar"><b>Nora Whitby</b>Professor</div>
</article>
<article class="instructor active" style="left:610px">
  <div class="active-frame">
    <b>Martin Hale</b><small>Vice Chancellor</small>
    <p>Lorem ipsum dolor sit amet ttuer<br>adipiscing elit sed diam.</p>
    <div class="socials"><i></i><i></i><i></i><i></i></div>
  </div>
</article>
<article class="instructor" style="left:843px">
  <div class="instructor-photo" role="img" aria-label="Portrait of a senior instructor in a shirt and striped tie"></div>
  <div class="name-bar"><b>Owen Pratt</b>Assistant Professor</div>
</article>

<footer class="site-footer">
  <p>Copyright © 2018 LearnHarbor. All Rights Reserved.</p>
  <div class="footer-social"><i style="background:#3b5998"></i><i style="background:#29a9e1"></i><i style="background:#0e76a8"></i><i style="background:#d23a2f"></i></div>
</footer>

</body>
</html>
```